2018 Fundraiser Event Flier

We are a non profit that works in the homeless community, The Lanternwick Guild. We offer a unique program of supported employment that is all about community engagement and building relationships not only with our participants but with community businesses and non profit partners. Our mission statement is "We seek and foster partnerships between the business and nonprofit communities to respectfully and effectively guide individuals from disenfranchised communities forward in sustainable employment to realize their potential of fully enriched lives for themselves and their families" We are having a fundraising event on Dec 13 and need a flier to advertise the event both via email and physical postings. We like a black background and bright colors (see uploaded example) and want to advertise the event and a small amount about who we are. Fun and bright. We will upload two of our logos and two photos that we have used in branding previously.

```html
<!DOCTYPE html>
<html lang="en">
<head>
<meta charset="utf-8">
<title>The Lanternwick Guild – Fundraising Event Flier</title>
<link rel="stylesheet" href="https://fonts.googleapis.com/css2?family=Delius&family=Yanone+Kaffeesatz:wght@600&family=Fredoka:wght@600&display=swap">
<style>
  :root {
    --board-dark: #2c2d2f;
    --board-mid: #3b3c3f;
    --lime: #8cc63f;
    --lime-deep: #79b12f;
    --sky: #a9d8ec;
    --paper: #f3f3f4;
    --paper-shade: #e2e2e5;
    --ink: #1f1f1f;
    --white: #ffffff;
    --skin-light: #e9b9a3;
    --skin-deep: #b9765a;
  }
  * { margin: 0; padding: 0; box-sizing: border-box; }
  html, body { width: 867px; height: 1200px; overflow: hidden; background: var(--paper); }
  .flier {
    position: relative;
    width: 867px;
    height: 1200px;
    overflow: hidden;
    background: linear-gradient(180deg, var(--paper) 0%, var(--paper-shade) 100%);
  }
  .flier__board {
    position: absolute;
    left: 0; top: 0;
    width: 867px; height: 874px;
    background: linear-gradient(90deg, var(--board-dark) 0%, var(--board-mid) 50%, var(--board-dark) 100%);
  }
  .brand-top {
    position: absolute;
    left: 0; top: 150px;
    width: 867px;
    text-align: center;
    font-family: "Fredoka", sans-serif;
    font-weight: 600;
    font-size: 46px;
    color: var(--lime);
    letter-spacing: 1px;
  }
  .brand-top__dot {
    display: inline-block;
    width: 22px; height: 22px;
    border-radius: 50%;
    background: var(--lime);
    margin-right: 14px;
    vertical-align: 4px;
  }
  .shapes { position: absolute; left: 0; top: 0; }
  .mission {
    position: absolute;
    left: 150px; top: 380px;
    width: 620px;
    text-align: center;
    font-family: "Delius", cursive;
    font-size: 19px;
    line-height: 36px;
    color: var(--white);
  }
  .hand {
    position: absolute;
  }
  .hand--left {
    left: 0; top: 690px;
    width: 400px; height: 120px;
    border-radius: 0 60px 60px 0;
    background: linear-gradient(90deg, var(--skin-deep) 0%, var(--skin-light) 100%);
  }
  .hand--right {
    left: 505px; top: 905px;
    width: 362px; height: 120px;
    border-radius: 60px 0 0 60px;
    background: linear-gradient(270deg, var(--skin-deep) 0%, var(--skin-light) 100%);
  }
  .event {
    position: absolute;
    left: 0; top: 800px;
    width: 867px;
    text-align: center;
    font-family: "Yanone Kaffeesatz", sans-serif;
    font-weight: 600;
    font-size: 70px;
    line-height: 72px;
    color: var(--lime);
    -webkit-text-stroke: 3px var(--white);
    paint-order: stroke fill;
    text-shadow: 0 4px 6px rgba(0,0,0,0.35);
  }
  .event sup { font-size: 36px; vertical-align: 26px; }
  .brand-bottom {
    position: absolute;
    left: 0; top: 1045px;
    width: 867px;
    text-align: center;
    font-family: "Fredoka", sans-serif;
    font-weight: 600;
    font-size: 50px;
    color: var(--ink);
  }
</style>
</head>
<body>
<main class="flier">
  <div class="flier__board"></div>

  <div class="brand-top"><span class="brand-top__dot"></span>The Lanternwick Guild</div>

  <svg class="shapes" width="867" height="900" viewBox="0 0 867 900" aria-hidden="true">
    <polygon points="58,352 138,340 98,288" fill="var(--sky)"/>
    <polygon points="64,410 99,413 88,386" fill="var(--lime)"/>
    <polygon points="717,649 749,664 719,677" fill="var(--lime)"/>
    <polygon points="652,748 725,744 705,687" fill="var(--sky)"/>
    <path class="bubble"
      d="M160,350 Q470,320 780,352 Q800,358 792,380 L708,660 Q698,700 660,704 L500,708 L452,758 L440,710 L250,712 Q212,712 200,680 L132,388 Q128,356 160,350 Z"
      fill="var(--lime)" stroke="var(--white)" stroke-width="6" stroke-linejoin="round"/>
  </svg>

  <p class="mission">"We Seek And Foster Partnerships Between The Business<br>And Nonprofit Communities To Respectfully &amp;<br>Effectively Guide Individuals From<br>Disenfranchised Communities Forward<br>In Sustainable Employment To Realize Their<br>Potential Of Fully<br>Enriched Lives For<br>Themselves And Their Families"</p>

  <div class="hand hand--left" role="img" aria-label="Illustrated hand reaching in from the left"></div>
  <div class="hand hand--right" role="img" aria-label="Illustrated hand reaching in from the right"></div>

  <h1 class="event">Fundraising Event on<br>13<sup>th</sup> December 2018</h1>

  <div class="brand-bottom">The Lanternwick Guild</div>
</main>
</body>
</html>
```